Web Site for Strategy and Technology Consulting Company

We are looking for a website design that engages potential customers to understand our services and contact us. In this contest, we are looking for a homepage design, but the winning designer will be favored for the design of some of the more complicated interior pages of the site. An additional contest (or contests) for these pages will be added soon.

PLATROM AND RESPONSIVE DESIGN
The site will be implemented in WordPress using the Elementor page builder.
We are looking for a design that will look good on phones are well as laptop browsers.

UPLOADED FILES INCLUDE:
1a A wireframe of the homepage we are looking for. The Uploaded PDF also includes a draft of the text proposed for the homepage. Designers are free to go beyond the wireframe, but all elements of the wireframe should be included.
1b A Word document with the draft text of the homepage.
2a-d The Norvalith logo. Two versions are included – a dark version which works well against a light background, and a light version which works well against a dark background.
3 The Norvalith color palette with HEX and RGB values. Designers are not limited to this palette, but colors should be complementary.
4 A draft of the homepage menu
5 Service sheets with information on the services we provide

MORE ABOUT NORVALITH
Norvalith is a consulting company focused on transforming businesses through software. Our tagline, “Transformation Delivered,” recognizes the gap business often have between business transformation and the software they end up with. By listening to our customers and understanding their vision and where they are, we help get our customers where they want to go.

We increase our capability by working with many consultants and partners, allowing us to provide our customers with the best people and the software that best suits them.

Industry/Entity Type

Consulting

Number of Pages Required

1 page

Font styles to use
Sans Serif

Requirements
Must have
• the content represented on the wireframe uploaded
Nice to have
• interactive features, such as roll-over icons that reveal additional information

```html
<!DOCTYPE html>
<html lang="en">
<head>
<meta charset="utf-8">
<title>Norvalith — Transformation Delivered</title>
<link href="https://fonts.googleapis.com/css2?family=DM+Sans:wght@400;500;700&display=swap" rel="stylesheet">
<style>
:root{
  --hero-a:#1f62d6;
  --hero-b:#5aa6ee;
  --accent:#2f8fe8;
  --accent-bright:#0f8cff;
  --navy:#1d5fa0;
  --band:#2a6cb4;
  --footer:#1e2f9e;
  --ink:#4a4a4a;
  --muted:#7a8594;
  --pale:#e6f2fd;
  --white:#ffffff;
  --gold:#f5c82a;
}
*{margin:0;padding:0;box-sizing:border-box}
html,body{width:1200px;height:4637px;overflow:hidden}
body{position:relative;font-family:'DM Sans',sans-serif;background:var(--white);color:var(--ink)}
.abs{position:absolute}
a{color:inherit;text-decoration:none}

/* hero */
.hero-bg{left:0;top:0;width:1200px;height:800px}
.nav{left:0;top:14px;width:1200px;height:32px}
.brand{font-weight:500;font-size:26px;color:var(--white);letter-spacing:-.5px}
.nav-links{left:523px;top:22px;display:flex;gap:18px;font-size:10px;color:var(--white)}
.nav-contact{left:913px;top:14px;width:78px;height:28px;border:1.5px solid var(--white);border-radius:6px;color:var(--white);font-size:9px;font-weight:700;display:flex;align-items:center;justify-content:center}
.hero-title{left:0;top:118px;width:1200px;text-align:center;font-size:52px;font-weight:700;color:var(--white);letter-spacing:-.5px}
.hero-sub{left:0;top:202px;width:1200px;text-align:center;font-size:14px;line-height:20px;color:#e4efff}
.btn{display:flex;align-items:center;justify-content:center;border-radius:7px;font-size:14px;font-weight:700}
.btn-start{left:468px;top:302px;width:138px;height:54px;background:#d6e8fb;color:#1d3f73}
.btn-trial{left:621px;top:302px;width:120px;height:54px;border:2px solid #d6e8fb;color:var(--white)}
.slide-no{left:156px;top:280px;font-size:58px;font-weight:500;color:var(--white)}
.progress{left:156px;top:400px;font-size:16px;color:#1b2f5e;font-weight:700;display:flex;align-items:center;gap:8px}
.progress span.track{width:114px;height:3px;background:var(--white);position:relative}
.progress span.track i{position:absolute;left:0;top:0;width:36px;height:3px;background:#0f6be0}
.side-tags{left:118px;top:490px;display:flex;flex-direction:column;gap:36px;font-size:12px;font-weight:700;color:var(--white)}
.side-tags span{transform:rotate(-90deg)}
.hero-photo{left:162px;top:465px;width:946px;height:495px;border-radius:18px;background:radial-gradient(circle at 48% 45%,#e0b36a 0,#8a5a35 18%,#2f3d4e 45%,#1c2633 100%);box-shadow:0 20px 40px rgba(20,40,90,.25)}
.hero-caption{left:162px;top:772px;width:714px;height:105px;background:rgba(70,130,200,.72);padding:18px 30px;font-size:31px;line-height:36px;color:var(--white)}
.hero-caption b{font-weight:500;color:var(--gold)}
.partner{top:1035px;height:52px;border-radius:8px;background:#e3e7ed}

/* technology */
.sec-title{left:0;top:1222px;width:1200px;text-align:center;font-size:52px;line-height:55px;font-weight:700;color:var(--navy)}
.sec-sub{left:0;top:1350px;width:1200px;text-align:center;font-size:14px;line-height:20px;color:var(--muted)}
.btn-work{left:534px;top:1422px;width:140px;height:54px;background:var(--accent);color:var(--white);font-size:14px}
.tech-art{left:470px;top:1530px;width:330px;height:440px;background:radial-gradient(circle at 50% 55%,#aebbd9 0,#6b85c4 35%,#e9eef8 70%,rgba(255,255,255,0) 72%)}
.icon-tile{width:56px;height:56px;border-radius:8px;background:linear-gradient(145deg,#2f7fe0,#1749b8);display:flex;align-items:center;justify-content:center}
.feat-title{font-size:21px;line-height:23px;font-weight:500;color:var(--navy)}
.feat-text{font-size:12px;line-height:18px;color:var(--muted);margin-top:4px}

/* people */
.people-title{left:148px;top:2506px;font-size:48px;font-weight:700;color:var(--white)}
.people-text{left:148px;top:2580px;width:300px;font-size:13px;line-height:19.5px;color:#e4efff}
.people-strong{left:148px;top:2716px;width:310px;font-size:13.5px;line-height:19.5px;font-weight:700;color:var(--white)}
.btn-team{left:148px;top:2795px;width:140px;height:54px;background:#6fb1f2;color:var(--white);font-size:14px}
.card-glass{left:498px;top:2431px;width:245px;height:349px;background:rgba(160,205,245,.45);border-radius:6px}
.card-white{left:774px;top:2300px;width:244px;height:347px;background:var(--white);border-radius:6px;box-shadow:0 10px 30px rgba(0,0,0,.15)}
.card-photo{border-radius:4px}
.card-note{font-size:11.5px;line-height:17px}

/* testimonials */
.quote-title{left:148px;top:3178px;width:400px;font-size:50px;line-height:54px;font-weight:500;color:var(--ink)}
.quote-sub{left:148px;top:3355px;width:370px;font-size:13px;line-height:22px;color:#8b8b8b}
.quote-card{top:3181px;width:346px;height:234px;background:var(--pale);border-radius:14px;padding:34px 38px}
.quote-card p{font-size:14px;line-height:26px;color:#8a8f98}
.quote-who{display:flex;align-items:center;gap:16px;margin-top:24px;font-size:16px;font-weight:700;color:#555}
.avatar{width:40px;height:40px;background:linear-gradient(135deg,#c99a72,#6b4a36)}
.arrow-dot{top:3446px;width:24px;height:24px;border-radius:50%;background:var(--accent);display:flex;align-items:center;justify-content:center}

/* cta */
.cta-bg{left:0;top:3600px;width:1200px;height:500px;background:#eef6fe}
.cta-title{left:0;top:3665px;width:1200px;text-align:center;font-size:46px;font-weight:500;color:var(--ink)}
.cta-sub{left:0;top:3748px;width:1200px;text-align:center;font-size:14px;line-height:20px;color:#6a6f78}
.btn-contact{left:540px;top:3823px;width:160px;height:54px;background:var(--accent);color:var(--white);font-size:15px}

/* footer */
.footer-brand{left:144px;top:4142px;font-size:28px;font-weight:500;color:var(--white)}
.footer-about{left:144px;top:4188px;width:270px;font-size:12.5px;line-height:18px;color:#dfe6ff}
.foot-col{top:4026px}
.foot-col h4{font-size:14px;font-weight:700;color:var(--white);margin-bottom:22px}
.foot-col li{list-style:none;font-size:12px;color:#dfe6ff;height:44px}
.social{top:4305px;width:38px;height:38px;border-radius:8px;background:rgba(255,255,255,.22);display:flex;align-items:center;justify-content:center}
.social i{width:12px;height:12px;border-radius:50%;background:var(--white)}
.foot-rule{left:140px;top:4562px;width:926px;height:1px;background:rgba(255,255,255,.3)}
.copyright{left:0;top:4584px;width:1200px;text-align:center;font-size:12px;color:#dfe6ff}
</style>
</head>
<body>

<!-- hero -->
<svg class="abs hero-bg" viewBox="0 0 1200 800" aria-hidden="true">
  <defs>
    <linearGradient id="heroGrad" x1="0" y1="0" x2="1" y2="1">
      <stop offset="0" stop-color="#1a55d0"/>
      <stop offset=".55" stop-color="#5aa6ee"/>
      <stop offset="1" stop-color="#3a6fe0"/>
    </linearGradient>
  </defs>
  <polygon points="0,0 1200,0 1200,560 0,780" fill="url(#heroGrad)"/>
  <polygon points="1090,140 1200,120 1200,190 1090,210" fill="#1778ff" opacity=".8"/>
  <polygon points="0,700 120,690 120,760 0,775" fill="#0f7aff" opacity=".8"/>
  <polygon points="0,245 188,220 188,340 0,370" fill="none" stroke="#bcd8ff" stroke-opacity=".5"/>
  <g fill="#ffffff">
    <circle cx="1033" cy="418" r="2.5"/><circle cx="1049" cy="418" r="2.5"/><circle cx="1065" cy="418" r="2.5"/><circle cx="1081" cy="418" r="2.5"/><circle cx="1097" cy="418" r="2.5"/><circle cx="1113" cy="418" r="2.5"/><circle cx="1129" cy="418" r="2.5"/>
    <circle cx="1033" cy="436" r="2.5"/><circle cx="1049" cy="436" r="2.5"/><circle cx="1065" cy="436" r="2.5"/><circle cx="1081" cy="436" r="2.5"/><circle cx="1097" cy="436" r="2.5"/><circle cx="1113" cy="436" r="2.5"/><circle cx="1129" cy="436" r="2.5"/>
    <circle cx="1033" cy="454" r="2.5"/><circle cx="1049" cy="454" r="2.5"/><circle cx="1065" cy="454" r="2.5"/><circle cx="1081" cy="454" r="2.5"/><circle cx="1097" cy="454" r="2.5"/><circle cx="1113" cy="454" r="2.5"/><circle cx="1129" cy="454" r="2.5"/>
    <circle cx="1033" cy="472" r="2.5"/><circle cx="1049" cy="472" r="2.5"/><circle cx="1065" cy="472" r="2.5"/><circle cx="1081" cy="472" r="2.5"/><circle cx="1097" cy="472" r="2.5"/><circle cx="1113" cy="472" r="2.5"/><circle cx="1129" cy="472" r="2.5"/>
    <circle cx="1033" cy="490" r="2.5"/><circle cx="1049" cy="490" r="2.5"/><circle cx="1065" cy="490" r="2.5"/><circle cx="1081" cy="490" r="2.5"/><circle cx="1097" cy="490" r="2.5"/><circle cx="1113" cy="490" r="2.5"/><circle cx="1129" cy="490" r="2.5"/>
    <circle cx="1033" cy="508" r="2.5"/><circle cx="1049" cy="508" r="2.5"/><circle cx="1065" cy="508" r="2.5"/><circle cx="1081" cy="508" r="2.5"/><circle cx="1097" cy="508" r="2.5"/><circle cx="1113" cy="508" r="2.5"/><circle cx="1129" cy="508" r="2.5"/>
  </g>
</svg>

<header>
  <div class="abs brand" style="left:86px;top:12px">Norvalith</div>
  <nav class="abs nav-links">
    <a>Home</a><a>About Us ⌄</a><a>Services ⌄</a><a>Insights ⌄</a><a>Join Us ⌄</a>
  </nav>
  <a class="abs nav-contact">Contact Us</a>
</header>

<section>
  <h1 class="abs hero-title">Transformation Delivered</h1>
  <p class="abs hero-sub">We do more for our customers than implement software. We listen.<br>We work to understand where they are in their transformation<br>journey and where they want to go.</p>
  <a class="abs btn btn-start">Start Now</a>
  <a class="abs btn btn-trial">Trial →</a>
  <div class="abs slide-no">01</div>
  <div class="abs progress">01 <span class="track"><i></i></span> <span style="color:#d9e7fb">04</span></div>
  <div class="abs side-tags"><span>DR</span><span>BH</span><span>IG</span></div>
  <div class="abs hero-photo" role="img" aria-label="Photo of cupped hands holding a glowing light bulb"></div>
  <div class="abs hero-caption">Focus on <b>business</b> value, with an emphasis on delivering <b>value</b> quickly.</div>
</section>

<!-- partner badges -->
<div class="abs partner" style="left:250px;width:122px"></div>
<div class="abs partner" style="left:470px;width:124px"></div>
<div class="abs partner" style="left:698px;width:106px;border-radius:26px"></div>
<div class="abs partner" style="left:908px;width:112px"></div>

<!-- technology -->
<svg class="abs" style="left:0;top:1190px" width="260" height="180" aria-hidden="true">
  <polygon points="0,20 220,0 220,80 0,105" fill="#eaf4fd"/>
  <polygon points="0,80 220,55 220,130 0,160" fill="none" stroke="#d6e6f5"/>
</svg>
<h2 class="abs sec-title">Transformation Supported<br>by Technology</h2>
<p class="abs sec-sub">We do more for our customers than implement software. We listen. We work to<br>understand where they are in their transformation journey and where they want to go.</p>
<a class="abs btn btn-work">How We Work</a>

<div class="abs tech-art" role="img" aria-label="3D letter A built from blue, yellow and grey cubes"></div>
<svg class="abs" style="left:0;top:1500px" width="1200" height="560" aria-hidden="true">
  <g fill="none" stroke="#2f7fe0" stroke-width="1.3" stroke-dasharray="4 3">
    <path d="M430,92 H480 V108 H560"/>
    <path d="M856,60 H780 V90 H720"/>
    <path d="M420,300 V302 H560"/>
    <path d="M845,250 V250 H730"/>
    <path d="M652,430 V260"/>
  </g>
</svg>

<div class="abs icon-tile" style="left:374px;top:1575px"><svg width="26" height="26" viewBox="0 0 26 26"><path d="M9 22h10M10 19h8l-1-7 2-3-3-4h-4l-3 4 2 3z" fill="none" stroke="#fff" stroke-width="1.6"/></svg></div>
<div class="abs" style="left:374px;top:1646px;width:170px">
  <div class="feat-title">Business<br>Transformation</div>
  <div class="feat-text">Define and execute your<br>strategy.</div>
</div>

<div class="abs icon-tile" style="left:800px;top:1556px"><svg width="26" height="26" viewBox="0 0 26 26"><rect x="4" y="5" width="18" height="16" rx="2" fill="none" stroke="#fff" stroke-width="1.6"/><path d="M8 10h6M8 14h6M8 18h4" stroke="#fff" stroke-width="1.4"/><circle cx="18" cy="12" r="2.5" fill="none" stroke="#fff" stroke-width="1.4"/></svg></div>
<div class="abs" style="left:800px;top:1626px;width:200px">
  <div class="feat-title">BI and Data</div>
  <div class="feat-text">Discover, connect, and trust<br>your data.</div>
</div>

<div class="abs icon-tile" style="left:261px;top:1800px"><svg width="26" height="26" viewBox="0 0 26 26"><rect x="3" y="5" width="20" height="13" rx="1.5" fill="none" stroke="#fff" stroke-width="1.6"/><path d="M10 22h6M13 18v4M7 9h5v5H7zM15 9h4M15 13h4" stroke="#fff" stroke-width="1.4" fill="none"/></svg></div>
<div class="abs" style="left:261px;top:1868px;width:200px">
  <div class="feat-title">ERP<br>Implementations</div>
  <div class="feat-text">Assess, upgrade, and<br>implement ERP solutions to<br>meet your needs.</div>
</div>

<div class="abs icon-tile" style="left:824px;top:1787px"><svg width="26" height="26" viewBox="0 0 26 26"><circle cx="13" cy="10" r="4" fill="none" stroke="#fff" stroke-width="1.6"/><path d="M5 21c1-4 4-6 8-6s7 2 8 6" fill="none" stroke="#fff" stroke-width="1.6"/></svg></div>
<div class="abs" style="left:824px;top:1856px;width:200px">
  <div class="feat-title">Building the Right<br>Team of People</div>
  <div class="feat-text">Hire resources for your<br>transformation journey.</div>
</div>

<div class="abs icon-tile" style="left:606px;top:1934px"><svg width="26" height="26" viewBox="0 0 26 26"><rect x="4" y="5" width="18" height="16" rx="2" fill="none" stroke="#fff" stroke-width="1.6"/><path d="M4 10h18M8 14h10M8 17h6" stroke="#fff" stroke-width="1.4"/></svg></div>
<div class="abs" style="left:606px;top:2003px;width:200px">
  <div class="feat-title">CRM<br>Implementations</div>
  <div class="feat-text">Take your relationships to<br>the next level.</div>
</div>

<!-- people band -->
<svg class="abs" style="left:0;top:2080px" width="1200" height="980" aria-hidden="true">
  <defs>
    <linearGradient id="bandGrad" x1="0" y1="0" x2="1" y2="0">
      <stop offset="0" stop-color="#2465ad"/>
      <stop offset="1" stop-color="#3a82c9"/>
    </linearGradient>
  </defs>
  <polygon points="0,215 1200,45 1200,760 0,940" fill="url(#bandGrad)"/>
  <polygon points="0,150 170,145 170,200 0,210" fill="none" stroke="#cfe4f6"/>
  <polygon points="1042,320 1200,290 1200,350 1042,380" fill="#1a8cff"/>
  <polygon points="0,650 130,625 130,700 0,725" fill="#1a8cff"/>
  <g fill="#d5e8fa">
    <circle cx="1072" cy="10" r="2.5"/><circle cx="1090" cy="10" r="2.5"/><circle cx="1108" cy="10" r="2.5"/><circle cx="1126" cy="10" r="2.5"/><circle cx="1144" cy="10" r="2.5"/><circle cx="1162" cy="10" r="2.5"/>
    <circle cx="1072" cy="28" r="2.5"/><circle cx="1090" cy="28" r="2.5"/><circle cx="1108" cy="28" r="2.5"/><circle cx="1126" cy="28" r="2.5"/><circle cx="1144" cy="28" r="2.5"/><circle cx="1162" cy="28" r="2.5"/>
    <circle cx="1072" cy="46" r="2.5"/><circle cx="1090" cy="46" r="2.5"/><circle cx="1108" cy="46" r="2.5"/><circle cx="1126" cy="46" r="2.5"/><circle cx="1144" cy="46" r="2.5"/><circle cx="1162" cy="46" r="2.5"/>
    <circle cx="1072" cy="64" r="2.5"/><circle cx="1090" cy="64" r="2.5"/><circle cx="1108" cy="64" r="2.5"/><circle cx="1126" cy="64" r="2.5"/><circle cx="1144" cy="64" r="2.5"/><circle cx="1162" cy="64" r="2.5"/>
    <circle cx="74" cy="870" r="2.5"/><circle cx="92" cy="870" r="2.5"/><circle cx="110" cy="870" r="2.5"/><circle cx="128" cy="870" r="2.5"/><circle cx="146" cy="870" r="2.5"/><circle cx="164" cy="870" r="2.5"/>
    <circle cx="74" cy="888" r="2.5"/><circle cx="92" cy="888" r="2.5"/><circle cx="110" cy="888" r="2.5"/><circle cx="128" cy="888" r="2.5"/><circle cx="146" cy="888" r="2.5"/><circle cx="164" cy="888" r="2.5"/>
    <circle cx="74" cy="906" r="2.5"/><circle cx="92" cy="906" r="2.5"/><circle cx="110" cy="906" r="2.5"/><circle cx="128" cy="906" r="2.5"/><circle cx="146" cy="906" r="2.5"/><circle cx="164" cy="906" r="2.5"/>
    <circle cx="74" cy="924" r="2.5"/><circle cx="92" cy="924" r="2.5"/><circle cx="110" cy="924" r="2.5"/><circle cx="128" cy="924" r="2.5"/><circle cx="146" cy="924" r="2.5"/><circle cx="164" cy="924" r="2.5"/>
    <circle cx="74" cy="942" r="2.5"/><circle cx="92" cy="942" r="2.5"/><circle cx="110" cy="942" r="2.5"/><circle cx="128" cy="942" r="2.5"/><circle cx="146" cy="942" r="2.5"/><circle cx="164" cy="942" r="2.5"/>
  </g>
</svg>

<h2 class="abs people-title">It’s the People</h2>
<p class="abs people-text">The world has changed in the past twenty years. The people you need might not all work for one company. Our clients want the best resources, available quickly. That’s why, in addition to our team of experts, we partner with:</p>
<p class="abs people-strong">People are invariably at the center of our customer’s success. Find out how we can add our experts to yours.</p>
<a class="abs btn btn-team">Our Team</a>

<div class="abs card-glass">
  <div class="abs card-photo" style="left:24px;top:25px;width:199px;height:204px;background:radial-gradient(circle at 60% 55%,#5b8fb8 0,#c9a060 30%,#3b2a20 70%,#1c1410 100%)" role="img" aria-label="Photo of a globe on a dark desk"></div>
  <p class="abs card-note" style="left:22px;top:250px;width:200px;color:#e8f2fc">Service providers all over the world to provide the resources and value that are right for you, available 24 x 7.</p>
</div>
<div class="abs card-white">
  <div class="abs card-photo" style="left:23px;top:25px;width:198px;height:203px;background:linear-gradient(160deg,#d8d2c8 0,#8aa0b4 45%,#3d5f80 100%)" role="img" aria-label="Photo of consultants working together in a bright office"></div>
  <p class="abs card-note" style="left:20px;top:250px;width:200px;color:#333">A large network of expert consultants who are the best at what they do.</p>
</div>

<!-- testimonials -->
<h2 class="abs quote-title">Join Other And See What Our Client Says</h2>
<p class="abs quote-sub">Lorem ipsum dolor sit amet consectetur adipiscing elit cursus ullamcorper netus facilisis cras ut sed sodales tellus ac urna enim vestib.</p>
<div class="abs quote-card" style="left:572px">
  <p>Lorem ipsum dolor sit amet consectetur adipiscing elit cursus ullamcorper netus facilisis cras ut sed sodales tellus ac urna enim vestib.</p>
  <div class="quote-who"><div class="avatar" role="img" aria-label="Client portrait"></div>Dorian Kessly</div>
</div>
<div class="abs quote-card" style="left:935px">
  <p>Lorem ipsum dolor sit amet consectetur adipiscing elit cursus ullamcorper netus facilisis cras ut sed sodales tellus ac urna enim vestib.</p>
  <div class="quote-who"><div class="avatar" role="img" aria-label="Client portrait"></div>Mira Tolvanen</div>
</div>
<div class="abs arrow-dot" style="left:1027px"><svg width="10" height="10"><path d="M7 1L3 5l4 4" fill="none" stroke="#fff" stroke-width="2"/></svg></div>
<div class="abs arrow-dot" style="left:1071px"><svg width="10" height="10"><path d="M3 1l4 4-4 4" fill="none" stroke="#fff" stroke-width="2"/></svg></div>

<!-- call to action -->
<div class="abs cta-bg"></div>
<svg class="abs" style="left:0;top:3900px" width="1200" height="737" aria-hidden="true">
  <polygon points="0,170 1200,65 1200,737 0,737" fill="var(--footer)"/>
  <polygon points="0,65 230,40 230,110 0,135" fill="none" stroke="#d6e6f5"/>
  <polygon points="993,60 1200,25 1200,100 993,135" fill="#1a8cff"/>
  <polygon points="0,600 95,585 95,640 0,655" fill="#1a8cff"/>
  <polygon points="1068,405 1200,385 1200,470 1068,490" fill="none" stroke="#6c7ad0"/>
</svg>
<h2 class="abs cta-title">Let's start growing your business</h2>
<p class="abs cta-sub">Lorem ipsum dolor sit amet, consectetur adipiscing elit.<br>Diam ut id nisl tellus rhoncus, imperdiet</p>
<a class="abs btn btn-contact">Contact Us Now</a>

<!-- footer -->
<footer>
  <div class="abs footer-brand">Norvalith</div>
  <p class="abs footer-about">Lorem ipsum dolor sit amet, consectetur adipiscing elit. Diam ut id nisl tellus rhoncus, imperdiet</p>
  <div class="abs foot-col" style="left:516px"><h4>Pages</h4><ul><li>Home</li><li>About Us</li><li>Services</li><li>Insights</li><li>Join Us</li></ul></div>
  <div class="abs foot-col" style="left:723px"><h4>Resources</h4><ul><li>Home</li><li>About Us</li><li>Services</li><li>Insights</li><li>Join Us</li></ul></div>
  <div class="abs foot-col" style="left:968px"><h4>Useful Links</h4><ul><li>Home</li><li>About Us</li><li>Services</li><li>Insights</li><li>Join Us</li></ul></div>
  <a class="abs social" style="left:143px" aria-label="Website"><i></i></a>
  <a class="abs social" style="left:197px" aria-label="Social profile"><i></i></a>
  <a class="abs social" style="left:251px" aria-label="Social profile"><i></i></a>
  <a class="abs social" style="left:305px" aria-label="Social profile"><i></i></a>
  <a class="abs social" style="left:359px" aria-label="Social profile"><i></i></a>
  <div class="abs foot-rule"></div>
  <p class="abs copyright">Copyright © 2023 Brightfold. Agreement and Privacy Policy.</p>
</footer>

</body>
</html>
```